Nordic Joinery Guild Wordpress Theme and newsletter template

We at the NJG are looking to start a Wordpress website and also send out a newsletter (web). We have just completed a Logo design project with ArtFlockly and we were so pleased with the results that we would like to see what the designers can come up with for a Wordpress theme and a template for an online newsletter. The theme has to support Icelandic letters. It also has to have a subscription option by email. We would need to have the option to add advertisement banners. The theme has to be easy to work with.
Below we have added a two websites for a example of what we are looking for: .
http://www.torvexhub.example/
http://www.brakkel.example/
The newsletter has to have a similar theme as the website and will be used with MS Publisher.

Attached is the new NJG logo.
Updates

Project Deadline Extended Reason: Not fully happy with the designs we have gotten so far. Would like to extend time to see if improvements can be made. Added Tuesday, June 16, 2015

Target Market(s)

Welding association members, welding and metalworking industry, suppliers in welding industry, International welding community, other national welding associations, welding education community

Industry/Entity Type

Welding

Number of Pages Required

3 page

Requirements
Must have
• The TKBÓ logo
• Icelandic letters
• email formpage
• Advertisement space/banners/buttons
• Easy to manage
• Compatible with Wordpress
Nice to have
• Welding pictures
• Nice graphics
Should not have
• Should not be dark and heavy set.

```html
<!DOCTYPE html>
<html lang="en">
<head>
<meta charset="utf-8">
<title>Welding Association</title>
<link href="https://fonts.googleapis.com/css2?family=Roboto:wght@400;500;700&family=Open+Sans:wght@400;600&display=swap" rel="stylesheet">
<style>
:root{
  --blue:#1a8cc7;
  --blue-dark:#1b5f9e;
  --navy:#2a4a7c;
  --red:#c62a2f;
  --red-bar:#c0282e;
  --text:#444;
  --muted:#666;
  --nav-bg:#f3f3f3;
  --white:#fff;
}
*{margin:0;padding:0;box-sizing:border-box}
html,body{width:741px;height:1200px;overflow:hidden;background:#fff}
body{position:relative;font-family:"Open Sans",sans-serif;color:var(--text)}
.abs{position:absolute}
.header{left:0;top:0;width:741px;height:81px;background:#fff}
.brand{left:61px;top:22px;display:flex;align-items:center;gap:6px}
.brand-mark{width:30px;height:30px;border-radius:50%;background:var(--red)}
.brand-name{font-family:"Roboto",sans-serif;font-weight:700;font-size:24px;color:var(--blue-dark);line-height:1}
.brand-sub{font-family:"Roboto",sans-serif;font-weight:700;font-size:5px;color:var(--blue-dark);margin-top:2px}
.contact{font-size:8.5px;line-height:14px;color:#444}
.icon-ring{width:26px;height:26px;border:1px solid #999;border-radius:50%;display:flex;align-items:center;justify-content:center}
.band{left:0;top:81px;width:741px;height:329px;background:var(--blue)}
.nav{left:61px;top:97px;width:619px;height:38px;background:var(--nav-bg);display:flex;font-family:"Roboto",sans-serif;font-size:9px;color:#555}
.nav span{display:flex;align-items:center;justify-content:center;border-right:1px solid #ddd;height:100%}
.nav span:last-child{border-right:none}
.hero{left:61px;top:135px;width:619px;height:300px;background:linear-gradient(100deg,#b3142a 0%,#d52a3a 45%,#7a2a3e 70%,#304050 100%)}
.hero-title{left:61px;top:92px;font-family:"Roboto",sans-serif;font-weight:700;color:#fff;font-size:37px;line-height:1}
.hero-sub{left:61px;top:129px;font-family:"Roboto",sans-serif;font-weight:700;color:#fff;font-size:25px}
.hero-text{left:60px;top:166px;width:250px;font-size:8.5px;line-height:14px;color:#fff}
.arrow{width:22px;height:22px;border-radius:50%;background:rgba(0,0,0,.35);display:flex;align-items:center;justify-content:center}
.welcome{left:0;top:464px;width:741px;text-align:center;font-family:"Roboto",sans-serif;font-size:19px;color:#333}
.welcome em{font-style:normal;color:var(--blue)}
.intro{left:125px;top:497px;width:491px;text-align:center;font-size:6.5px;line-height:13px;color:#555}
.card{top:556px;width:191px}
.card-img{height:113px}
.card h3{font-family:"Roboto",sans-serif;font-weight:400;font-size:8px;color:#333;margin-top:14px}
.card p{font-size:6.5px;line-height:13px;color:#666;margin-top:5px}
.more{font-family:"Roboto",sans-serif;font-size:7.5px;color:var(--blue-dark);text-decoration:underline;display:block;margin-top:8px}
.sec-title{font-family:"Roboto",sans-serif;font-size:16px;color:var(--blue-dark)}
.sec-title .hl{color:var(--red)}
.rule{height:1px;background:#e6e6e6}
.members-img{left:61px;top:840px;width:160px;height:140px;background:linear-gradient(135deg,#6d8fb0,#c9a56a 55%,#c63a3a)}
.members-text{left:236px;top:838px;width:244px;font-size:6.5px;line-height:13px;color:#444}
.news{left:507px;width:180px}
.news h4{font-family:"Open Sans",sans-serif;font-weight:400;font-size:9px;color:var(--blue-dark)}
.news .time{font-size:7px;color:#555;margin-top:7px;display:flex;align-items:center;gap:4px}
.news p{font-size:7px;line-height:14px;color:#555;margin-top:5px;letter-spacing:.2px}
.footer{left:0;top:1010px;width:741px;height:190px;background:var(--blue);color:#fff}
.footer h5{font-family:"Roboto",sans-serif;font-weight:400;font-size:9px;letter-spacing:.2px}
.footer .col{position:absolute;top:23px;font-size:7px;line-height:13px}
.footer ul{list-style:none;margin-top:13px;font-size:7.5px;line-height:15px}
.field{width:139px;height:26px;background:#fff;color:#666;font-size:6.5px;padding:8px 8px}
.btn{width:56px;height:22px;background:var(--red);color:#fff;font-size:6.5px;display:flex;align-items:center;justify-content:center;margin-top:6px}
.social{display:flex;gap:4px;margin-top:12px}
.social i{width:15px;height:15px;border:1px solid #fff;border-radius:50%;display:block}
.bottom{left:61px;top:1162px;width:619px;height:38px;background:var(--red-bar);color:#fff;font-size:6.5px;display:flex;align-items:center;justify-content:center}
</style>
</head>
<body>
<header class="abs header">
  <div class="abs brand">
    <span class="brand-mark"></span>
    <div>
      <div class="brand-name">TKBÓ</div>
      <div class="brand-sub">TRÉSMÍÐAFÉLAG BÓRÐA</div>
    </div>
  </div>
  <div class="abs icon-ring" style="left:378px;top:30px">
    <svg width="11" height="11" viewBox="0 0 24 24"><path d="M6.6 10.8c1.4 2.8 3.8 5.1 6.6 6.6l2.2-2.2c.3-.3.7-.4 1-.2 1.1.4 2.3.6 3.6.6.6 0 1 .4 1 1V20c0 .6-.4 1-1 1C10.6 21 3 13.4 3 4c0-.6.4-1 1-1h3.5c.6 0 1 .4 1 1 0 1.3.2 2.5.6 3.6.1.3 0 .7-.2 1L6.6 10.8z" fill="#555"/></svg>
  </div>
  <div class="abs contact" style="left:413px;top:29px">Ph: (03) 7142 6690<br>hello@joinerguildmail.example</div>
  <div class="abs icon-ring" style="left:558px;top:30px">
    <svg width="10" height="12" viewBox="0 0 20 24"><path d="M10 0C5 0 1.5 3.7 1.5 8.3 1.5 14.5 10 24 10 24s8.5-9.5 8.5-15.7C18.5 3.7 15 0 10 0zm0 11.5a3.2 3.2 0 110-6.4 3.2 3.2 0 010 6.4z" fill="#555"/></svg>
  </div>
  <div class="abs contact" style="left:594px;top:28px">48-62 Carrow Lane<br>Fernhill, QLD, 4812</div>
</header>

<div class="abs band"></div>

<nav class="abs nav">
  <span style="width:79px">Home</span>
  <span style="width:80px">About us</span>
  <span style="width:81px">Members</span>
  <span style="width:125px">Metalworking Industry</span>
  <span style="width:80px">Welding</span>
  <span style="width:82px">Services</span>
  <span style="width:92px">Contact us</span>
</nav>

<section class="abs hero" role="img" aria-label="Welder in a protective mask working amid flying sparks">
  <div class="abs hero-title">WELDING</div>
  <div class="abs hero-sub">Association</div>
  <p class="abs hero-text">Lorem ipsum dolor sit amet, consectetur adipiscing elit, sed do eiusmod tempor incididunt ut labore et dolore magna aliqua. Ut enim ad minim veniam, quis nostrud</p>
  <div class="abs arrow" style="left:18px;top:139px"><svg width="8" height="10" viewBox="0 0 8 10"><path d="M6 1L2 5l4 4" stroke="#fff" stroke-width="1.6" fill="none"/></svg></div>
  <div class="abs arrow" style="left:580px;top:139px"><svg width="8" height="10" viewBox="0 0 8 10"><path d="M2 1l4 4-4 4" stroke="#fff" stroke-width="1.6" fill="none"/></svg></div>
</section>

<h1 class="abs welcome">Welcome To <em>Welding Association</em></h1>
<p class="abs intro">Vestibulum commodo volutpat a, convallis ac, laoreet enim. Phasellus fermentum in, dolor pellentesque. Mulla imperdiet sit amet magna. Vestibulum dapibus, Vestibulum commodo volutpat a, convallis ac, laoreet enim. Phasellus fermentum in, dolor pellentesque. Mulla imperdiet sit amet magna. Vestibulum dapibus, Vestibulum commodo volutpat a, convallis ac, laoreet enim. Phasellus fermentum in,</p>

<article class="abs card" style="left:61px">
  <div class="card-img" role="img" aria-label="Worker cutting metal with an angle grinder and sparks" style="background:linear-gradient(135deg,#e8e4e0,#c23a35 50%,#e9a25a)"></div>
  <h3>WELDING AND METALWORKING INDUSTRY</h3>
  <p>Lorem ipsum dolor sit amet, consectetur adipiscing elit, sed do eiusmod tempor incididunt ut labore et dolore magna Lorem ipsum dolor sit amet.</p>
  <a class="more">READ MORE</a>
</article>
<article class="abs card" style="left:276px">
  <div class="card-img" role="img" aria-label="Close-up of a grinder throwing golden sparks" style="background:linear-gradient(135deg,#3a3a3a,#d89a3a 55%,#f2c65a)"></div>
  <h3>SUPPLIERS IN WELDING INDUSTRY</h3>
  <p>Lorem ipsum dolor sit amet, consectetur adipiscing elit, sed do eiusmod tempor incididunt ut labore et dolore magna Lorem ipsum dolor sit amet.</p>
  <a class="more">READ MORE</a>
</article>
<article class="abs card" style="left:490px">
  <div class="card-img" role="img" aria-label="Two workers in hard hats at an industrial site" style="background:linear-gradient(135deg,#8d959c,#2f3e6a 55%,#b9bec2)"></div>
  <h3>INTERNATIONAL WELDING COMMUNITY</h3>
  <p>Lorem ipsum dolor sit amet, consectetur adipiscing elit, sed do eiusmod tempor incididunt ut labore et dolore magna Lorem ipsum dolor sit amet.</p>
  <a class="more">READ MORE</a>
</article>

<h2 class="abs sec-title" style="left:61px;top:796px">Welding Association Members</h2>
<div class="abs rule" style="left:61px;top:824px;width:415px"></div>
<div class="abs members-img" role="img" aria-label="Worker in a yellow hard hat servicing machinery"></div>
<div class="abs members-text">
  <p>Lorem ipsum dolor sit amet, consectetur adipiscing elit, sed do eiusmod tempor incididunt ut labore et dolore magna aliqua. Ut enim ad minim veniam, quis nostrud exercitation&nbsp; Lorem ipsum dolor sit amet, consectetur adipiscing elit, sed do eiusmod tempor incididunt ut labore et dolore magna aliqua. Ut enim ad minim veniam,</p>
  <p style="margin-top:6px">Lorem ipsum dolor sit amet, consectetur adipiscing elit, sed do eiusmod tempor incididunt ut labore et dolore magna aliqua. Ut enim ad minim veniam, quis nostrud exercitation&nbsp; Lorem ipsum dolor sit amet, consectetur adipiscing elit, sed do eiusmod tempor incididunt</p>
  <p style="margin-top:11px;font-family:Roboto,sans-serif;font-size:8.5px;color:var(--navy);display:flex;align-items:center;gap:8px">READ MORE <svg width="8" height="8" viewBox="0 0 8 8"><circle cx="4" cy="4" r="4" fill="#2a4a7c"/><path d="M3.2 2.2L5 4 3.2 5.8" stroke="#fff" stroke-width="1.1" fill="none"/></svg></p>
</div>

<h2 class="abs sec-title" style="left:508px;top:796px">Latest <span class="hl">News</span></h2>
<div class="abs rule" style="left:507px;top:824px;width:174px"></div>
<div class="abs news" style="top:836px">
  <h4>Nemo Enim Ipsam Voluptatem</h4>
  <div class="time"><svg width="7" height="7" viewBox="0 0 8 8"><circle cx="4" cy="4" r="3.3" stroke="#333" fill="none"/><path d="M4 2v2h1.5" stroke="#333" fill="none"/></svg>19.00 pm - 21.00 pm</div>
  <p>Vivamus elementum semper nisi.&nbsp; Lorem ipsum dolor sit amet, sectetuer adipiscing elit.</p>
</div>
<div class="abs news" style="top:921px">
  <h4>Nemo Enim Ipsam Voluptatem</h4>
  <div class="time"><svg width="7" height="7" viewBox="0 0 8 8"><circle cx="4" cy="4" r="3.3" stroke="#333" fill="none"/><path d="M4 2v2h1.5" stroke="#333" fill="none"/></svg>19.00 pm - 21.00 pm</div>
  <p>Vivamus elementum semper nisi.&nbsp; Lorem ipsum dolor sit amet, sectetuer adipiscing elit.</p>
</div>

<footer class="abs footer">
  <div class="col" style="left:61px;width:130px">
    <h5>WELDING ASSOCIATION</h5>
    <p style="margin-top:13px">Lorem ipsum dolor sit amet, consectetur adipiscing elit, sed do eiusmod tempor incididunt ut labore et dolore magna aliqua. Ut enim ad minim veniam, quis nostrud exercitation ullamco laboris</p>
  </div>
  <div class="col" style="left:213px">
    <h5>QUICK LINKS</h5>
    <ul><li>Home</li><li>About us</li><li>suppliers in welding industry</li><li>International welding community</li><li>Meet our Team</li><li>Contact us</li></ul>
  </div>
  <div class="col" style="left:360px;width:145px">
    <h5>SIGN UP FOR NEWSLETTER</h5>
    <p style="margin-top:9px">Excepteur sint occaecat cupidatat non dent, sunt in culpa qui officia</p>
    <div class="field" style="margin-top:9px">Enter Name</div>
    <div class="btn">SUBSCRIBE</div>
  </div>
  <div class="col" style="left:536px;width:150px">
    <h5>CONTACT US</h5>
    <p style="margin-top:9px;font-size:7.5px">welding association PO Box 3318, Dunmore NSW 2419</p>
    <p style="margin-top:8px;font-size:8px;display:flex;align-items:center;gap:9px"><svg width="11" height="11" viewBox="0 0 24 24"><path d="M6.6 10.8c1.4 2.8 3.8 5.1 6.6 6.6l2.2-2.2c.3-.3.7-.4 1-.2 1.1.4 2.3.6 3.6.6.6 0 1 .4 1 1V20c0 .6-.4 1-1 1C10.6 21 3 13.4 3 4c0-.6.4-1 1-1h3.5c.6 0 1 .4 1 1 0 1.3.2 2.5.6 3.6.1.3 0 .7-.2 1L6.6 10.8z" fill="none" stroke="#fff" stroke-width="1.5"/></svg>+1 0512 448 207</p>
    <p style="margin-top:2px;font-size:8px;display:flex;align-items:center;gap:9px"><svg width="11" height="9" viewBox="0 0 12 9"><rect x=".5" y=".5" width="11" height="8" fill="none" stroke="#fff"/><path d="M.5.5L6 5l5.5-4.5" fill="none" stroke="#fff"/></svg>hello@joinerguildmail.example</p>
    <div class="social"><i></i><i></i><i></i><i></i><i></i></div>
  </div>
</footer>
<div class="abs bottom">©2014 - 2015&nbsp; WELDING ASSOCIATION.. All Rights Reserved.</div>
</body>
</html>
```